Private Optometric Practice Needs new Presentation Folders/Stationary

We recently moved our office and are looking to refresh our presentation folders and stationary. I tend to prefer simple, clean designs. We are a full scope optometric practice provide high quality eyewear, custom contact lenses, along with emergency care and treatment for dry eyes. We communicate with a lot of other doctors and want to exude professionalism. I have attached 2 versions of our logo.

Target Market(s)

Familys

Industry/Entity Type

Eyecare

Font styles to use
Sans Serif

Colors
0054AA
0677BA
7BADD7
CADEEF
E8F1F8

Requirements
Nice to have
• Bifold, areas to put information about practice, welcome letter

```html
<!DOCTYPE html>
<html lang="en">
<head>
<meta charset="utf-8">
<title>Northgate Vision – Stationery</title>
<link href="https://fonts.googleapis.com/css2?family=Montserrat:wght@400;500;600&display=swap" rel="stylesheet">
<style>
  :root{
    --slate:#34434e;
    --slate-dark:#2c3a44;
    --aqua:#5ec4ea;
    --paper:#f7f8f9;
    --paper-shade:#eceeef;
    --ground:#eef0f1;
    --ink-light:#e6ecef;
    --ink-dark:#55606a;
  }
  *{box-sizing:border-box;margin:0;padding:0}
  html,body{width:1200px;height:800px;overflow:hidden}
  body{background:var(--ground);font-family:"Montserrat",sans-serif;position:relative}
  .piece{position:absolute;box-shadow:0 2px 8px rgba(0,0,0,.12)}

  .brand{display:flex;flex-direction:column;align-items:center;text-align:center;color:var(--ink-light);font-weight:400;letter-spacing:.22em;line-height:1.15}
  .brand-dot{border-radius:50%;background:var(--aqua);display:block}

  /* Letterhead */
  .letterhead{left:310px;top:75px;width:333px;height:473px;background:var(--paper)}
  .letterhead-header{height:68px;background:var(--slate);border-bottom:3px solid var(--aqua);padding-top:9px}
  .letterhead-header .brand-dot{width:22px;height:22px;margin-bottom:5px}
  .letterhead-header .brand-name{font-size:11px}
  .letterhead-footer{position:absolute;left:0;bottom:0;width:100%;height:38px;background:var(--slate);border-top:3px solid var(--aqua);display:flex;justify-content:space-between;padding:6px 16px 0;color:var(--ink-light);font-size:6.5px;line-height:1.35;letter-spacing:.04em}
  .contact-line{display:flex;align-items:center;gap:5px}
  .contact-line svg{width:7px;height:7px;fill:currentColor}

  /* Folder */
  .folder{left:663px;top:50px;width:366px;height:498px;background:var(--slate)}
  .folder-band{position:absolute;left:316px;top:0;width:2px;height:100%;background:var(--aqua)}
  .folder-spine{position:absolute;left:318px;top:0;width:48px;height:100%;background:var(--slate-dark);opacity:.5}
  .folder .brand{position:absolute;left:0;top:160px;width:316px}
  .folder .brand-dot{width:86px;height:86px;margin-bottom:26px}
  .folder .brand-name{font-size:34px;letter-spacing:.2em}

  /* Business cards */
  .card{left:160px;width:130px;height:78px}
  .card-front{top:577px;background:var(--paper);display:flex;padding:10px 6px}
  .card-front .brand{width:52px;color:var(--slate);letter-spacing:.14em;justify-content:center}
  .card-front .brand-dot{width:12px;height:12px;margin-bottom:3px}
  .card-front .brand-name{font-size:5.5px}
  .card-details{border-left:1px solid #cfd4d7;padding-left:6px;font-size:4.3px;color:var(--ink-dark);line-height:1.5}
  .card-details .person{font-size:5px;font-weight:500;margin-bottom:3px;letter-spacing:.04em}
  .card-back{top:668px;height:80px;background:var(--slate);display:flex;align-items:center;justify-content:center}
  .card-back .brand{letter-spacing:.16em}
  .card-back .brand-dot{width:24px;height:24px;margin-bottom:4px}
  .card-back .brand-name{font-size:6px}

  /* Square envelope */
  .envelope-square{left:311px;top:572px;width:347px;height:175px;background:var(--paper);display:flex}
  .envelope-square-panel{width:159px;height:100%;background:var(--slate);padding:20px 0 0 32px;color:var(--ink-light)}
  .envelope-square-panel .brand{align-items:center;width:96px;letter-spacing:.2em}
  .envelope-square-panel .brand-dot{width:34px;height:34px;margin-bottom:6px}
  .envelope-square-panel .brand-name{font-size:10px}
  .envelope-address{margin-top:26px;font-size:5.5px;line-height:1.45;letter-spacing:.04em}
  .envelope-square-panel .contact-line{font-size:5.5px;margin-top:2px}
  .envelope-square-panel .contact-block{margin-top:8px}

  /* Long envelope */
  .envelope-long{left:675px;top:572px;width:377px;height:173px;background:var(--paper)}
  .envelope-flap{height:46px;border-bottom:1px solid #d9dcde;background:var(--paper-shade);border-radius:0 0 14px 14px;display:flex;justify-content:space-between;padding:10px 48px 0 32px;font-size:5.5px;color:var(--ink-dark);line-height:1.45;letter-spacing:.04em}
  .envelope-long .brand{margin-top:20px;color:var(--slate);letter-spacing:.2em}
  .envelope-long .brand-dot{width:46px;height:46px;margin-bottom:10px}
  .envelope-long .brand-name{font-size:13px}
</style>
</head>
<body>

<svg width="0" height="0" style="position:absolute">
  <symbol id="icon-phone" viewBox="0 0 24 24"><path d="M6.6 10.8a15.1 15.1 0 0 0 6.6 6.6l2.2-2.2c.3-.3.7-.4 1-.2 1.1.4 2.3.6 3.6.6.6 0 1 .4 1 1V20c0 .6-.4 1-1 1A17 17 0 0 1 3 4c0-.6.4-1 1-1h3.5c.6 0 1 .4 1 1 0 1.3.2 2.5.6 3.6.1.3 0 .7-.2 1z"/></symbol>
  <symbol id="icon-globe" viewBox="0 0 24 24"><path d="M12 2a10 10 0 1 0 0 20 10 10 0 0 0 0-20zm6.9 6h-3a15.7 15.7 0 0 0-1.3-3.6A8 8 0 0 1 18.9 8zM12 4c.8 1.2 1.5 2.5 1.9 4h-3.8c.4-1.5 1.1-2.8 1.9-4zM4.3 14a8.2 8.2 0 0 1 0-4h3.4a16.5 16.5 0 0 0 0 4zm.8 2h3a15.7 15.7 0 0 0 1.3 3.6A8 8 0 0 1 5.1 16zm3-8h-3a8 8 0 0 1 4.3-3.6C8.9 5.5 8.4 6.7 8.1 8zM12 20c-.8-1.2-1.5-2.5-1.9-4h3.8c-.4 1.5-1.1 2.8-1.9 4zm2.3-6H9.7a14.7 14.7 0 0 1 0-4h4.6a14.7 14.7 0 0 1 0 4zm.3 5.6c.6-1.1 1-2.3 1.3-3.6h3a8 8 0 0 1-4.3 3.6zm1.7-5.6a16.5 16.5 0 0 0 0-4h3.4a8.2 8.2 0 0 1 0 4z"/></symbol>
</svg>

<!-- Letterhead -->
<section class="piece letterhead">
  <header class="letterhead-header">
    <div class="brand"><span class="brand-dot"></span><span class="brand-name">NORTHGATE<br>VISION</span></div>
  </header>
  <footer class="letterhead-footer">
    <address style="font-style:normal">4120 LAKEVIEW AVE.<br>SUITE B<br>FAIRMONT, MI 48201</address>
    <div>
      <div class="contact-line"><svg><use href="#icon-phone"/></svg>555-014-2290</div>
      <div class="contact-line"><svg><use href="#icon-globe"/></svg>WWW.NORTHGATEVISION.COM</div>
    </div>
  </footer>
</section>

<!-- Presentation folder -->
<section class="piece folder">
  <div class="folder-spine"></div>
  <div class="folder-band"></div>
  <div class="brand"><span class="brand-dot"></span><span class="brand-name">NORTHGATE<br>VISION</span></div>
</section>

<!-- Business card front -->
<section class="piece card card-front">
  <div class="brand"><span class="brand-dot"></span><span class="brand-name">NORTHGATE<br>VISION</span></div>
  <div class="card-details">
    <div class="person">DANIEL HARTWELL, O.D.</div>
    <div>Doctor of Optometry</div>
    <div>4120 Lakeview Ave. Suite B</div>
    <div>Fairmont, MI 48201</div>
    <div style="margin-top:3px">555-014-2290</div>
    <div>dh@northgatevision.com</div>
  </div>
</section>

<!-- Business card back -->
<section class="piece card card-back">
  <div class="brand"><span class="brand-dot"></span><span class="brand-name">NORTHGATE VISION</span></div>
</section>

<!-- Square envelope -->
<section class="piece envelope-square">
  <div class="envelope-square-panel">
    <div class="brand"><span class="brand-dot"></span><span class="brand-name">NORTHGATE<br>VISION</span></div>
    <address class="envelope-address" style="font-style:normal">4120 LAKEVIEW AVE.<br>SUITE B<br>FAIRMONT, MI 48201</address>
    <div class="contact-block">
      <div class="contact-line"><svg><use href="#icon-phone"/></svg>555-014-2290</div>
      <div class="contact-line"><svg><use href="#icon-globe"/></svg>WWW.NORTHGATEVISION.COM</div>
    </div>
  </div>
</section>

<!-- Long envelope -->
<section class="piece envelope-long">
  <div class="envelope-flap">
    <address style="font-style:normal">4120 LAKEVIEW AVE.<br>SUITE B<br>FAIRMONT, MI 48201</address>
    <div>
      <div class="contact-line"><svg><use href="#icon-phone"/></svg>555-014-2290</div>
      <div class="contact-line"><svg><use href="#icon-globe"/></svg>WWW.NORTHGATEVISION.COM</div>
    </div>
  </div>
  <div class="brand"><span class="brand-dot"></span><span class="brand-name">NORTHGATE VISION</span></div>
</section>

</body>
</html>
```